Stationary Set Rebrand for Brenvik

We are a Canadian Distribution and Service Company that was established in 1969. Over the past 5 decades we have expanded our business and have warehouses across Canada. We specialize in adhesive tapes, adhesives, films, safety, warehouse, shipping, janitorial and packaging supplies.

We have updated our logo design and would like a new corporate branding identity that includes a new fresh Stationary Set (Business Cards, Letterhead, Letterhead MS Word, Envelope, Presentation Folders, Email Signatures, Notepad Covers, etc.)

Target Market(s)

Industrial Business Sector

Font styles to use
Sans Serif

Colors
0054AA
0677BA
7BADD7
CADEEF
E8F1F8
0094D4
00A9DD
6FCCEA
C7EBF8
E9F6FB
00AB8E
00BBA5
67D7C9
C6EFE9
E9F9F6
EB3D1F
EC4F4E
F09395
F8D3D4
FCEDEE

Requirements
Should not have
• Colors not too light, darker colours preferred

```html
<!DOCTYPE html>
<html lang="en">
<head>
<meta charset="utf-8">
<title>Brenvik Stationery Set</title>
<link href="https://fonts.googleapis.com/css2?family=Montserrat:wght@400;500;600;800&display=swap" rel="stylesheet">
<style>
  :root {
    --red: #d71920;
    --black: #0a0a0a;
    --white: #ffffff;
    --backdrop: #d6d6d6;
    --text: #222222;
    --rule-grey: #555555;
    --shadow: 7px 9px 10px rgba(0,0,0,.38);
  }
  * { box-sizing: border-box; margin: 0; padding: 0; }
  html, body { width: 916px; height: 1200px; overflow: hidden; }
  body { background: var(--backdrop); font-family: "Montserrat", Arial, sans-serif; color: var(--text); position: relative; }

  .piece { position: absolute; background: var(--white); box-shadow: var(--shadow); overflow: hidden; }

  .logo { position: absolute; display: flex; flex-direction: column; align-items: flex-start; line-height: 1; }
  .logo-row { display: flex; align-items: flex-end; gap: 3px; }
  .logo-name { font-weight: 800; color: var(--black); letter-spacing: -0.5px; }
  .logo-mark { background: var(--red); display: inline-block; }
  .logo-tag { font-weight: 600; color: var(--black); margin-top: 1px; white-space: nowrap; }

  .contacts { position: absolute; list-style: none; font-size: 10px; line-height: 1.25; white-space: nowrap; }
  .contacts li { display: flex; align-items: flex-start; gap: 7px; margin-bottom: 4px; }
  .contacts li:last-child { margin-bottom: 0; }
  .contacts svg { width: 8px; height: 8px; flex: none; margin-top: 2px; fill: var(--red); }

  .stripe { position: absolute; display: block; }
  .person-name { position: absolute; color: var(--red); font-weight: 600; text-transform: uppercase; }

  .rule { position: absolute; height: 1px; background: linear-gradient(to right, var(--rule-grey) 50%, var(--red) 50%); }

  .card-front { left: 38px; top: 52px; width: 368px; height: 215px; }
  .card-back  { left: 38px; top: 314px; width: 368px; height: 215px; }
  .folder     { left: 38px; top: 576px; width: 368px; height: 477px; }
  .letterhead { left: 425px; top: 52px; width: 454px; height: 642px; }
  .email-sig  { left: 425px; top: 741px; width: 454px; height: 105px; }
  .envelope   { left: 425px; top: 893px; width: 454px; height: 226px; }

  .email-divider { position: absolute; left: 205px; top: 13px; width: 1px; height: 82px; background: linear-gradient(var(--rule-grey), var(--red)); }
  .email-sig .contacts { font-size: 8.5px; line-height: 1.7; }
  .email-sig .contacts li { margin-bottom: 0; gap: 6px; }
  .email-sig .contacts svg { margin-top: 3px; width: 7px; height: 7px; }
</style>
</head>
<body>

<svg width="0" height="0" style="position:absolute" aria-hidden="true">
  <defs>
    <symbol id="ic-phone" viewBox="0 0 10 10"><path d="M2 0.5 L3.6 2.6 L2.8 3.6 C3.5 5 4.8 6.4 6.4 7.2 L7.4 6.4 L9.5 8 L8.4 9.5 C4.5 9.3 0.7 5.5 0.5 1.6 Z"/></symbol>
    <symbol id="ic-mail" viewBox="0 0 10 10"><path d="M0 2 H10 V8.5 H0 Z M0.6 2.4 L5 5.6 L9.4 2.4" stroke="#fff" stroke-width="0.8"/></symbol>
    <symbol id="ic-web" viewBox="0 0 10 10"><circle cx="5" cy="5" r="4.5"/><path d="M0.8 5 H9.2 M5 0.6 C2.8 3 2.8 7 5 9.4 M5 0.6 C7.2 3 7.2 7 5 9.4" stroke="#fff" stroke-width="0.7" fill="none"/></symbol>
    <symbol id="ic-pin" viewBox="0 0 10 10"><path d="M5 0.3 C2.9 0.3 1.5 1.9 1.5 3.8 C1.5 6.3 5 9.7 5 9.7 C5 9.7 8.5 6.3 8.5 3.8 C8.5 1.9 7.1 0.3 5 0.3 Z"/><circle cx="5" cy="3.8" r="1.3" fill="#fff"/></symbol>
  </defs>
</svg>

<!-- Business card front -->
<section class="piece card-front">
  <div class="logo" style="right:30px; top:22px;">
    <div class="logo-row"><span class="logo-name" style="font-size:34px;">Brenvik</span><span class="logo-mark" style="width:7px;height:7px;margin-bottom:6px;"></span></div>
    <span class="logo-tag" style="font-size:7px;">Tape and Packaging Specialists</span>
  </div>
  <h1 class="person-name" style="left:22px; top:86px; font-size:17px;">Mara Ellison</h1>
  <ul class="contacts" style="left:23px; top:126px;">
    <li><svg><use href="#ic-phone"/></svg>(555) 014-2200</li>
    <li><svg><use href="#ic-mail"/></svg>mara@brenvik.com</li>
    <li><svg><use href="#ic-web"/></svg>www.brenvik.com</li>
    <li><svg><use href="#ic-pin"/></svg><span>218 Harbour Line Rd #<br>B4 Suite, Millbrook, ON K0L 2H0</span></li>
  </ul>
  <svg class="stripe" style="right:0; bottom:23px;" width="146" height="14" viewBox="0 0 146 14">
    <polygon points="10,0 52,0 42,14 0,14" fill="var(--black)"/>
    <polygon points="52,0 146,0 146,14 42,14" fill="var(--red)"/>
  </svg>
</section>

<!-- Business card back -->
<section class="piece card-back">
  <svg class="stripe" style="right:0; top:24px;" width="134" height="14" viewBox="0 0 134 14">
    <polygon points="10,0 36,0 26,14 0,14" fill="var(--black)"/>
    <polygon points="36,0 134,0 134,14 26,14" fill="var(--red)"/>
  </svg>
  <div class="logo" style="left:80px; top:72px;">
    <div class="logo-row"><span class="logo-name" style="font-size:50px;">Brenvik</span><span class="logo-mark" style="width:10px;height:10px;margin-bottom:9px;"></span></div>
    <span class="logo-tag" style="font-size:10px;">Tape and Packaging Specialists</span>
  </div>
  <svg class="stripe" style="left:0; top:180px;" width="134" height="14" viewBox="0 0 134 14">
    <polygon points="0,0 112,0 102,14 0,14" fill="var(--red)"/>
    <polygon points="112,0 134,0 124,14 102,14" fill="var(--black)"/>
  </svg>
</section>

<!-- Presentation folder -->
<section class="piece folder">
  <svg style="position:absolute;left:0;top:0;" width="368" height="477" viewBox="0 0 386 499" preserveAspectRatio="none">
    <polygon points="0,0 386,0 386,256 0,60" fill="var(--red)"/>
    <polygon points="0,70 110,126 45,212 0,194" fill="var(--black)"/>
    <polygon points="326,243 386,274 386,410 215,376" fill="var(--red)"/>
    <polygon points="0,284 386,480 386,499 0,499" fill="var(--black)"/>
  </svg>
  <div class="logo" style="left:50px; top:212px;">
    <div class="logo-row"><span class="logo-name" style="font-size:52px;">Brenvik</span><span class="logo-mark" style="width:10px;height:10px;margin-bottom:9px;"></span></div>
    <span class="logo-tag" style="font-size:10.5px;">Tape and Packaging Specialists</span>
  </div>
</section>

<!-- Letterhead -->
<section class="piece letterhead">
  <div class="logo" style="left:160px; top:20px;">
    <div class="logo-row"><span class="logo-name" style="font-size:31px;">Brenvik</span><span class="logo-mark" style="width:6px;height:6px;margin-bottom:6px;"></span></div>
    <span class="logo-tag" style="font-size:6.5px;">Tape and Packaging Specialists</span>
  </div>
  <div class="rule" style="left:57px; top:70px; width:340px;"></div>
  <ul class="contacts" style="left:27px; top:548px; font-size:9.5px;">
    <li><svg><use href="#ic-phone"/></svg>(555) 014-2200</li>
    <li><svg><use href="#ic-mail"/></svg>mara@brenvik.com</li>
    <li><svg><use href="#ic-web"/></svg>www.brenvik.com</li>
    <li><svg><use href="#ic-pin"/></svg><span>218 Harbour Line Rd #<br>B4 Suite, Millbrook, ON K0L 2H0</span></li>
  </ul>
  <svg class="stripe" style="right:0; bottom:24px;" width="134" height="13" viewBox="0 0 134 13">
    <polygon points="10,0 42,0 32,13 0,13" fill="var(--black)"/>
    <polygon points="42,0 134,0 134,13 32,13" fill="var(--red)"/>
  </svg>
</section>

<!-- Email signature -->
<section class="piece email-sig">
  <div class="logo" style="left:40px; top:36px;">
    <div class="logo-row"><span class="logo-name" style="font-size:28px;">Brenvik</span><span class="logo-mark" style="width:6px;height:6px;margin-bottom:5px;"></span></div>
    <span class="logo-tag" style="font-size:6px;">Tape and Packaging Specialists</span>
  </div>
  <div class="email-divider"></div>
  <h2 class="person-name" style="left:227px; top:20px; font-size:14px;">Mara Ellison</h2>
  <ul class="contacts" style="left:227px; top:46px;">
    <li><svg><use href="#ic-phone"/></svg>(555) 014-2200</li>
    <li><svg><use href="#ic-mail"/></svg>mara@brenvik.com</li>
    <li><svg><use href="#ic-web"/></svg>www.brenvik.com</li>
  </ul>
  <ul class="contacts" style="left:330px; top:46px;">
    <li><svg><use href="#ic-pin"/></svg><span>218 Harbour Line Rd #<br>B4 Suite, Millbrook,<br>ON K0L 2H0</span></li>
  </ul>
</section>

<!-- Envelope -->
<section class="piece envelope">
  <div class="logo" style="left:165px; top:18px;">
    <div class="logo-row"><span class="logo-name" style="font-size:29px;">Brenvik</span><span class="logo-mark" style="width:6px;height:6px;margin-bottom:5px;"></span></div>
    <span class="logo-tag" style="font-size:6.5px;">Tape and Packaging Specialists</span>
  </div>
  <div class="rule" style="left:65px; top:66px; width:325px;"></div>
  <ul class="contacts" style="left:36px; top:126px; font-size:9.5px;">
    <li><svg><use href="#ic-phone"/></svg>(555) 014-2200</li>
    <li><svg><use href="#ic-mail"/></svg>mara@brenvik.com</li>
    <li><svg><use href="#ic-web"/></svg>www.brenvik.com</li>
    <li><svg><use href="#ic-pin"/></svg><span>218 Harbour Line Rd #<br>B4 Suite, Millbrook, ON K0L 2H0</span></li>
  </ul>
  <svg class="stripe" style="right:0; bottom:36px;" width="127" height="12" viewBox="0 0 127 12">
    <polygon points="9,0 40,0 31,12 0,12" fill="var(--black)"/>
    <polygon points="40,0 127,0 127,12 31,12" fill="var(--red)"/>
  </svg>
</section>

</body>
</html>
```